Brookfern Clinical Trials Redesign

Website name: http://brookfernclinicaltrials.example/live/
Industry: medical & pharmaceutical
Target audience:
Clinical research patients
clinical research sponsors
clinical research referring doctors
Style/theme of your website design:
We want to customize the orbitel theme, emulating our competitors website
http://templatemarket.example/item/orbitel-responsive-multipurpose-wordpress-theme/4417203
Webdesign Examples?
http://www.tmxclinical.example/currently-enrolling-clinical-trials/
https://www.copperwellresearch.example/
What do you like about these sites:
These sites address all the needs of a clinical trial facility. The patient, the doctor and the sponsor. Also they have forms and sign up information for each trial they offer. The site needs to have SCHEMA markup and rich snippets. We have reviews and testimonial that need schema markup also, local NAP information and all the other rich snippet markups available.
How many pages need design:
8-12
List any colors:
existing color of website and logo
Target Market(s)
Target audience:
Industry/Entity Type
Pharmaceutical
Number of Pages Required
5+ page
Look and feel

```html
<!DOCTYPE html>
<html lang="en">
<head>
<meta charset="utf-8">
<title>Brookfern Clinical Trials</title>
<link href="https://fonts.googleapis.com/css2?family=Open+Sans:wght@400;600;700;800&family=Montserrat:wght@600;700&display=swap" rel="stylesheet">
<style>
:root{
  --teal:#35bdae;
  --teal-dark:#239d90;
  --teal-deep:#1e8b80;
  --ink:#2e3336;
  --muted:#7c8488;
  --line:#e4e8ea;
  --white:#ffffff;
  --footer:#2fb1a3;
  --footer-bar:#26998c;
}
*{margin:0;padding:0;box-sizing:border-box}
html,body{width:1200px;height:2920px;overflow:hidden}
body{font-family:"Open Sans",Arial,sans-serif;color:var(--ink);background:var(--white)}
h1,h2,h3,h4{font-family:"Montserrat","Open Sans",sans-serif}

/* header */
.site-header{height:112px;display:flex;align-items:center;justify-content:space-between;padding:0 60px 0 48px;background:var(--white)}
.brand{display:flex;align-items:center;gap:12px;color:var(--teal);font-weight:700;font-size:26px;line-height:1}
.brand-mark{width:34px;height:34px;border-radius:50%;background:var(--teal)}
.main-nav{display:flex;gap:34px;font-size:15px;font-weight:700;letter-spacing:.3px}
.main-nav a{color:var(--ink);text-decoration:none}
.main-nav a.active{color:var(--teal)}

/* hero */
.hero{position:relative;height:488px;background:linear-gradient(100deg,#dfe9ec 0%,#eef4f5 45%,#c9dadf 100%)}
.hero-photo{position:absolute;inset:0}
.hero-card{position:absolute;left:100px;top:148px;width:220px;padding:26px 24px 26px;background:rgba(53,189,174,.88);color:var(--white)}
.hero-card .kicker{font-size:22px;font-weight:400;letter-spacing:.5px}
.hero-card h1{font-size:32px;font-weight:700;line-height:1.1;margin-top:4px;letter-spacing:.5px}
.btn-dark{display:inline-block;margin-top:18px;padding:10px 16px;background:#1f2426;color:var(--white);font-size:14px;font-weight:700;letter-spacing:.5px}
.hero-arrows{position:absolute;left:100px;bottom:34px;display:flex;gap:6px}
.hero-arrows span{width:40px;height:40px;background:#1f2426;display:flex;align-items:center;justify-content:center}

/* conditions */
.conditions{height:348px;display:flex;justify-content:center;gap:36px;padding-top:70px}
.condition{width:232px;text-align:center}
.condition .icon{width:96px;height:96px;border-radius:50%;border:2px solid #d8dcde;margin:0 auto 18px;display:flex;align-items:center;justify-content:center}
.condition .icon.filled{background:var(--teal);border-color:var(--teal)}
.condition h3{font-size:20px;font-weight:700;margin-bottom:10px}
.condition p{font-size:12px;line-height:1.6;color:var(--muted)}

/* teal bands */
.band{position:relative;color:var(--white);text-align:center;background:linear-gradient(100deg,#45c8b9 0%,#35bdae 50%,#2aaea0 100%)}
.band-photo{position:absolute;inset:0}
.band-inner{position:relative;padding:0 170px}
.band h2{font-size:31px;font-weight:700;letter-spacing:.4px}
.band p{font-size:13px;line-height:1.7;margin:14px auto 0;max-width:860px;opacity:.95}
.btn-outline{display:inline-block;margin-top:26px;padding:13px 26px;border:2px solid var(--white);font-size:13px;font-weight:700;letter-spacing:.5px}
.band-benefits{height:352px;padding-top:104px}
.band-choose{height:360px;padding-top:112px;background:linear-gradient(100deg,#3cc2b3 0%,#33bbac 55%,#2db3a5 100%)}

/* who can participate */
.eligibility{height:420px;position:relative;display:flex;align-items:center;padding-left:100px}
.eligibility-text{width:520px}
.eligibility h2{font-size:38px;font-weight:700;line-height:1.15}
.eligibility p{font-size:13px;line-height:1.7;color:var(--muted);margin-top:18px}
.btn-teal{display:inline-block;margin-top:22px;padding:12px 20px;background:var(--teal);color:var(--white);font-size:13px;font-weight:700}
.eligibility-photo{position:absolute;right:60px;top:20px;width:520px;height:400px;background:linear-gradient(180deg,#f3f5f6 0%,#e2eaec 100%)}

/* how it works */
.how{height:460px;text-align:center;padding-top:88px}
.how h2{font-size:38px;font-weight:700}
.steps{position:relative;display:flex;justify-content:space-between;width:880px;margin:60px auto 0}
.steps-line{position:absolute;left:110px;right:110px;top:57px;height:14px;background:var(--teal)}
.step{position:relative;width:260px}
.step .icon{width:128px;height:128px;border-radius:50%;background:var(--teal);margin:0 auto;display:flex;align-items:center;justify-content:center}
.step h3{font-size:22px;font-weight:700;margin-top:28px}
.step p{font-size:12px;line-height:1.6;color:var(--muted);margin-top:10px}

/* footer */
.site-footer{height:340px;background:var(--footer);color:var(--white);display:flex;gap:58px;padding:52px 40px 0 50px}
.footer-col h4{font-size:19px;font-weight:700;margin-bottom:18px;letter-spacing:.3px}
.footer-col{font-size:12px;line-height:1.7}
.col-social{width:190px}
.socials{display:flex;gap:6px}
.socials span{width:22px;height:22px;background:#1f7d73}
.socials span:nth-child(2){background:#e07b3b}
.socials span:nth-child(3){background:#3a7fc0}
.socials span:nth-child(4){background:#c94a3f}
.col-posts{width:270px}
.post{display:flex;gap:14px;margin-bottom:18px}
.post-thumb{width:64px;height:64px;border-radius:50%;background:linear-gradient(135deg,#cfe4e8,#8fc9c2);flex:none}
.post strong{display:block;font-size:13px}
.col-links{width:200px}
.col-links ul{list-style:none}
.col-contact{width:250px}
.footer-bar{height:40px;background:var(--footer-bar);color:var(--white);font-size:11px;display:flex;align-items:center;justify-content:center}
</style>
</head>
<body>

<header class="site-header">
  <div class="brand"><span class="brand-mark"></span>Brookfern Clinical Trials</div>
  <nav class="main-nav">
    <a class="active" href="#">HOME</a><a href="#">ABOUT US</a><a href="#">ABOUT CLINICAL TRIALS</a><a href="#">TRIALS</a><a href="#">PARTICIPATE</a><a href="#">CONTACT</a><a href="#">FAQS</a>
  </nav>
</header>

<section class="hero">
  <div class="hero-photo" role="img" aria-label="Photo of a doctor in surgical cap and mask in a bright clinic"></div>
  <div class="hero-card">
    <div class="kicker">JOINING A</div>
    <h1>CLINICAL TRIAL</h1>
    <span class="btn-dark">GET STARTED</span>
  </div>
  <div class="hero-arrows">
    <span><svg width="14" height="14" viewBox="0 0 14 14"><path d="M9 2 4 7l5 5" fill="none" stroke="#fff" stroke-width="2"/></svg></span>
    <span><svg width="14" height="14" viewBox="0 0 14 14"><path d="M5 2l5 5-5 5" fill="none" stroke="#fff" stroke-width="2"/></svg></span>
  </div>
</section>

<section class="conditions">
  <div class="condition">
    <div class="icon filled"><svg width="44" height="44" viewBox="0 0 44 44" fill="none" stroke="#fff" stroke-width="2.5"><rect x="7" y="9" width="30" height="28" rx="4"/><path d="M14 19a8 8 0 0 1 16 0"/><path d="M22 19l3-4"/></svg></div>
    <h3>WEIGHT LOSS</h3>
    <p>Current studies for adults working toward a healthy weight with guided care and regular checkups.</p>
  </div>
  <div class="condition">
    <div class="icon"><svg width="44" height="44" viewBox="0 0 44 44" fill="none" stroke="#8a9296" stroke-width="2.5"><path d="M22 36S7 27 7 16a8 8 0 0 1 15-4 8 8 0 0 1 15 4c0 11-15 20-15 20z"/></svg></div>
    <h3>HEART DISEASE</h3>
    <p>Research for people living with heart conditions, with close monitoring from our cardiac team.</p>
  </div>
  <div class="condition">
    <div class="icon"><svg width="44" height="44" viewBox="0 0 44 44" fill="none" stroke="#8a9296" stroke-width="2.5"><path d="M22 6c7 10 11 16 11 21a11 11 0 0 1-22 0c0-5 4-11 11-21z"/></svg></div>
    <h3>HIGH CHOLESTEROL</h3>
    <p>Trials testing new ways to lower cholesterol levels, open to qualified adult volunteers.</p>
  </div>
  <div class="condition">
    <div class="icon"><svg width="44" height="44" viewBox="0 0 44 44" fill="none" stroke="#8a9296" stroke-width="2.5"><path d="M30 8l6 6M33 11 16 28l-6-6 17-17M10 34l3-3M13 25l6 6"/></svg></div>
    <h3>TYPE II DIABETES</h3>
    <p>Studies for adults managing type II diabetes, including blood sugar review at each visit.</p>
  </div>
</section>

<section class="band band-benefits">
  <div class="band-photo" role="img" aria-label="Faded teal photo of a DNA strand and a doctor"></div>
  <div class="band-inner">
    <h2>WHAT ARE THE BENEFITS AND RISKS OF JOINING A TRIAL?</h2>
    <p>Taking part in a study gives you access to new treatments and expert care. Every trial also carries some risks, and our staff explain each one clearly before you decide to enroll.</p>
    <span class="btn-outline">VIEW DETAILS</span>
  </div>
</section>

<section class="eligibility">
  <div class="eligibility-text">
    <h2>WHO CAN PARTICIPATE IN A CLINICAL TRIAL?</h2>
    <p>All trials have guidelines about who can take part. Factors that allow someone to join a study are called inclusion criteria, and factors that rule someone out are called exclusion criteria. These include age, health history and current condition.</p>
    <span class="btn-teal">READ MORE</span>
  </div>
  <div class="eligibility-photo" role="img" aria-label="Photo of a smiling doctor with stethoscope presenting with an open hand"></div>
</section>

<section class="band band-choose">
  <div class="band-photo" role="img" aria-label="Faded teal photo of medical staff at work"></div>
  <div class="band-inner">
    <h2>CHOOSE TO PARTICIPATE?</h2>
    <p>When you choose to join, our coordinators guide you through screening, consent and every visit. You may leave a study at any time, and your care team will support you along the way.</p>
    <span class="btn-outline">VIEW DETAILS</span>
  </div>
</section>

<section class="how">
  <h2>HOW IT WORKS</h2>
  <div class="steps">
    <div class="steps-line"></div>
    <div class="step">
      <div class="icon"><svg width="56" height="56" viewBox="0 0 56 56" fill="none" stroke="#fff" stroke-width="3"><rect x="12" y="8" width="32" height="42" rx="3"/><path d="M18 38l7-9 6 5 8-12"/></svg></div>
      <h3>LOREM IPSUM</h3>
      <p>Review open studies and find one that fits your health needs.</p>
    </div>
    <div class="step">
      <div class="icon"><svg width="56" height="56" viewBox="0 0 56 56" fill="none" stroke="#fff" stroke-width="3"><rect x="10" y="10" width="36" height="36" rx="4"/><path d="M18 28l7 7 13-14"/></svg></div>
      <h3>LOREM IPSUM</h3>
      <p>Complete a short screening visit with our friendly research staff.</p>
    </div>
    <div class="step">
      <div class="icon"><svg width="56" height="56" viewBox="0 0 56 56" fill="none" stroke="#fff" stroke-width="3"><path d="M16 8v14a10 10 0 0 0 20 0V8"/><path d="M26 32v6a8 8 0 0 0 16 0v-4"/><circle cx="42" cy="30" r="4"/></svg></div>
      <h3>LOREM IPSUM</h3>
      <p>Attend scheduled visits and receive care from our medical team.</p>
    </div>
  </div>
</section>

<footer class="site-footer">
  <div class="footer-col col-social">
    <h4>STAY IN TOUCH</h4>
    <div class="socials"><span></span><span></span><span></span><span></span></div>
  </div>
  <div class="footer-col col-posts">
    <h4>LATEST POSTS</h4>
    <div class="post"><div class="post-thumb" role="img" aria-label="Thumbnail photo of clinic staff"></div><div><strong>Lorem ipsum dolor</strong>Apr 18, 2015<br>New study now enrolling.</div></div>
    <div class="post"><div class="post-thumb" role="img" aria-label="Thumbnail photo of a research team"></div><div><strong>Lorem ipsum dolor</strong>Apr 02, 2015<br>Meet our research team.</div></div>
  </div>
  <div class="footer-col col-links">
    <h4>QUICK LINKS</h4>
    <ul><li>Home</li><li>About Us</li><li>About Clinical Trials</li><li>Trials</li><li>Participate</li><li>Contact</li><li>FAQS</li></ul>
  </div>
  <div class="footer-col col-contact">
    <h4>CONTACT US</h4>
    <p>418 Brookfern Parkway, Suite 200<br>Fernvale, CA 90000</p>
    <p style="margin-top:12px">(555) 014-2287<br>info@brookfernclinicaltrials.example</p>
  </div>
</footer>
<div class="footer-bar">© Copyright 2015 Brookfern Clinical Trials. All rights reserved.</div>

</body>
</html>
```